New design for a hotel booking website

I am looking to re-design my hotel booking website pinecrestlodgings.net. Please find the specs attached. Delivery in PSD format. Two pages total: (i) homepage and (ii) inner page.
I want the design to be very simple to navigate and have a feel that is related to Banff, Canada. You can keep a similar layout as the current website.
Requirements
1) Homepage
- Booking form above the fold containing the check in & check out dates, # of rooms and the Search button
- Quality image relating to the city of Banff to make it clear what city this is (no slider - I don't want any animation)
- A section for featured hotels (3-5 items)
- A section for links to other sections on the website (currently under "Explore Banff")
- A section for articles and local guides
- A weather widget (either in the header or somewhere else, similar to this one http://clipvuebox.com/t/QX7RKLd4P2)
2) Hotel listings page - http://www.pinecrestlodgings.net/hotels
- Left or right sidebar – must contain the booking form with the same fields as on the homepage
- A section of why to book hotels with us under the booking form
- Each hotel listing should contain the following
Hotel name
Star rating
Short description (same as currently on the website)
Thumbnail
Address
A button to Check Rates
Notes
- I want the design to be user friendly, simple and easy to use
- I want it to be related to Banff. Banff is a resort town in Alberta, Canada with mountains for skiing in the winter and parks and wildlife nature in the summer.
- Delivery format: PSD
- I want the layout to be easily convertible into a responsive design
- Small social media icon to the Chatterly page (with the option to add Vidloom and Quibbit in the future)
Some competing website examples:
1) ridgemoorvale.com/Places-to-Stay/Hotels-Inns
2) torvikinns.org
Some examples of websites I liked:
1) http://www.glendrova.com/accommodation/hotels/
2) http://www.lodgetrailmarvenby.com/
Anyone looking to book their stay in Banff, AB, Canada.
Travel
2 page

```html
<!DOCTYPE html>
<html lang="en">
<head>
<meta charset="utf-8">
<title>Pinecrest Lodgings – Compare Prices on Accommodations in Banff</title>
<link href="https://fonts.googleapis.com/css2?family=Oswald:wght@400;500;600&family=Open+Sans:wght@400;600;700&display=swap" rel="stylesheet">
<style>
:root{
  --blue:#0a9fe0;
  --blue-dark:#1b7fcf;
  --blue-text:#1a8fd6;
  --yellow:#f6c400;
  --ink:#222;
  --body:#333;
  --muted:#666;
  --grey-band:#ebebeb;
  --white:#fff;
  --footer-bottom:#f6c400;
}
*{box-sizing:border-box;margin:0;padding:0}
html,body{width:1200px;height:3041px;overflow:hidden;background:var(--white)}
body{font-family:"Open Sans",Verdana,sans-serif;color:var(--body);font-size:13px;line-height:1.55;position:relative}
.wrap{width:1038px;margin:0 auto;position:relative;height:100%}

/* top bar + header */
.topbar{height:30px;background:var(--blue);color:#fff;font-size:14px}
.topbar .wrap{display:flex;justify-content:flex-end;align-items:center;gap:28px}
.topbar span{display:flex;align-items:center;gap:8px}
.header{height:75px;background:#fff;border-bottom:1px solid #ddd}
.header .wrap{display:flex;justify-content:space-between;align-items:center}
.brand-name{font-family:"Oswald",Arial,sans-serif;font-size:34px;font-weight:600;color:var(--blue-dark);line-height:1;letter-spacing:.3px}
.brand-tag{font-size:11px;color:var(--blue-text);letter-spacing:.3px;font-weight:600;margin-top:3px}
.nav{display:flex;gap:40px;align-self:flex-end;margin-bottom:14px}
.nav a{font-family:"Oswald",Arial,sans-serif;font-size:16px;color:#333;text-decoration:none;position:relative;padding-bottom:4px}
.nav a.active{color:var(--blue-text);border-bottom:3px solid var(--blue-text)}

/* hero */
.hero{height:447px;position:relative;background:linear-gradient(180deg,#a9c7d8 0%,#5e8a6f 22%,#3f6b4c 40%,#3aa7b8 58%,#2d9db4 100%)}
.hero-text{position:absolute;top:205px;left:0;right:0;text-align:center;color:#fff;text-shadow:0 2px 4px rgba(0,0,0,.45)}
.hero-text h1{font-family:"Oswald",Arial,sans-serif;font-size:32px;font-weight:500;letter-spacing:.5px}
.hero-text p{font-family:"Oswald",Arial,sans-serif;font-size:24px;font-weight:400;margin-top:2px}

/* booking bar */
.booking{height:86px;background:var(--blue)}
.booking .wrap{display:flex;align-items:center;gap:8px}
.booking-title{display:flex;align-items:center;gap:14px;width:210px;color:var(--yellow);font-family:"Oswald",Arial,sans-serif;font-size:27px;line-height:1.1;font-weight:500}
.field{height:40px;background:#fff;border-radius:3px;display:flex;align-items:center;justify-content:space-between;padding:0 10px;font-size:13px;color:#555}
.f-loc{width:204px}.f-date{width:152px}.f-rooms{width:118px}
.btn-check{height:40px;width:230px;background:var(--yellow);color:#222;font-family:"Oswald",Arial,sans-serif;font-size:16px;display:flex;align-items:center;justify-content:center;border-radius:3px;margin-left:8px}

/* section titles */
.sec-title{font-family:"Oswald",Arial,sans-serif;font-size:32px;font-weight:400;color:var(--ink);border-left:7px solid var(--yellow);padding-left:14px;line-height:42px}
.sec-title b{font-weight:600}

/* welcome */
.welcome{height:386px}
.welcome .sec-title{position:absolute;top:44px;left:0;font-size:32px}
.welcome .sec-title b{color:var(--blue-text);font-weight:500}
.welcome-text{position:absolute;top:104px;left:0;width:750px;font-size:12.5px;line-height:20.5px}
.btn{display:inline-flex;align-items:center;justify-content:center;border-radius:3px;font-size:13px;font-family:"Oswald",Arial,sans-serif;letter-spacing:.3px}
.btn-solid{background:var(--blue-dark);color:#fff}
.btn-line{border:2px solid var(--blue-dark);color:var(--blue-dark);background:#fff}
.welcome .read-more{position:absolute;top:275px;left:0;width:110px;height:34px;font-size:14px}
.weather{position:absolute;top:57px;right:0;width:227px;height:250px;border:2px solid #ddd;border-radius:8px;overflow:hidden;background:#fff}
.weather-top{height:155px;background:linear-gradient(135deg,#f9d84a,#f3b500);position:relative;color:#fff}
.weather-top .city{position:absolute;top:10px;left:14px;font-size:13px;font-weight:600}
.weather-top .unit{position:absolute;top:10px;right:14px;font-size:13px;font-weight:600}
.weather-top .temp{position:absolute;top:52px;left:104px;font-size:42px;font-weight:600;font-family:"Oswald",Arial,sans-serif}
.weather-days{display:flex;justify-content:space-around;padding-top:18px}
.day{text-align:center;font-size:11px;color:#555}

/* featured */
.featured{height:577px;background:var(--grey-band)}
.featured .sec-title{position:absolute;top:44px;left:0}
.cards{position:absolute;top:115px;left:0;display:flex;gap:40px}
.card{width:319px}
.card-img{height:215px;position:relative}
.card-head{display:flex;justify-content:space-between;align-items:baseline;margin-top:12px}
.card-head h3{font-family:"Oswald",Arial,sans-serif;font-weight:400;font-size:22px;color:#222}
.card-head .price{font-family:"Oswald",Arial,sans-serif;font-size:20px;color:var(--blue-text)}
.stars{display:flex;gap:3px;margin-top:4px}
.card p{font-size:12px;margin-top:6px;line-height:18px}
.card p b{display:block}
.card-actions{display:flex;gap:20px;margin-top:12px}
.card-actions .btn{width:107px;height:28px;font-size:13px}
.card-actions .btn-solid{width:108px}
.badge{position:absolute;top:-2px;right:22px}
.pager{position:absolute;top:528px;left:476px;display:flex;gap:12px}
.pager span{width:38px;height:32px;border:2px solid #555;display:flex;align-items:center;justify-content:center;background:#fff}

/* articles */
.articles{height:629px}
.articles .sec-title{position:absolute;top:50px;left:0}
.lead{position:absolute;top:117px;left:0;width:463px}
.lead-img{height:343px;position:relative}
.date{position:absolute;top:22px;right:0;width:45px;height:55px;background:var(--yellow);text-align:center;font-family:"Oswald",Arial,sans-serif;line-height:1.05;padding-top:6px;color:#222}
.date b{display:block;font-size:22px;font-weight:500}
.date span{font-size:15px}
.lead h3,.item h3{font-family:"Oswald",Arial,sans-serif;font-weight:400;color:var(--blue-text);font-size:22px}
.lead h3{margin-top:16px}
.lead p{font-size:12.5px;line-height:21px;margin-top:8px}
.more{color:var(--blue-text);font-weight:700}
.list{position:absolute;top:117px;left:509px;width:529px;display:flex;flex-direction:column;gap:42px}
.item{display:flex;gap:36px;height:127px}
.item-img{width:182px;height:127px;flex:none;position:relative}
.item-img .date{top:10px}
.item p{font-size:12.5px;line-height:20.5px;margin-top:8px}

/* why */
.why{height:334px;background:var(--blue);color:#fff}
.why .sec-title{position:absolute;top:32px;left:0;right:0;margin:0 auto;width:560px;color:#fff;font-size:31px}
.why-cols{position:absolute;top:110px;left:0;right:0;display:flex;justify-content:space-between}
.why-col{width:240px;text-align:center}
.why-col h4{font-family:"Oswald",Arial,sans-serif;font-weight:400;font-size:20px;margin-top:18px}
.why-col p{font-size:12.5px;line-height:20px;margin-top:12px;padding:0 4px}

/* newsletter */
.news{height:138px}
.news h2{position:absolute;top:20px;left:0;font-family:"Oswald",Arial,sans-serif;font-weight:400;font-size:24px;color:#222}
.news-form{position:absolute;top:66px;left:0;width:555px;height:36px;display:flex;border:1px solid #ccc;border-radius:3px;overflow:hidden}
.news-form span{flex:1;padding:0 12px;display:flex;align-items:center;font-size:12px;color:#888}
.news-form i{width:56px;background:var(--yellow);display:flex;align-items:center;justify-content:center}
.follow{position:absolute;top:52px;right:0;display:flex;align-items:center;gap:16px}
.follow .label{font-size:16px;color:#222;margin-right:60px}
.social{display:flex;align-items:center;gap:6px;font-size:13px;font-weight:600;color:var(--blue-dark)}
.social i{width:14px;height:14px;border-radius:50%;background:var(--blue-dark);display:block}

/* footer */
.footer{height:304px;background:linear-gradient(180deg,#2a8fb6 0%,#1f7ea4 45%,#196a8a 100%);color:#fff}
.f-cols{position:absolute;top:26px;left:0;right:0;display:flex}
.f-col h5{font-family:"Oswald",Arial,sans-serif;font-weight:400;font-size:19px;margin-bottom:10px}
.f-col h5 b{color:var(--yellow);font-weight:400}
.f-col ul{list-style:none}
.f-col li{font-size:13px;line-height:26px}
.f-explore{width:294px}.f-explore li{text-decoration:underline}
.f-quick{width:214px}
.f-contact{width:336px}
.c-row{display:flex;gap:14px;align-items:flex-start;font-size:13px;margin-bottom:18px;line-height:20px}
.c-row i{width:24px;height:24px;border-radius:50%;background:#fff;flex:none;display:flex;align-items:center;justify-content:center}
.gallery{display:grid;grid-template-columns:93px 93px;gap:12px 12px}
.gallery div{height:61px;border:2px solid var(--yellow)}
.g-arrows{display:flex;gap:8px;justify-content:center;margin-top:12px}
.g-arrows span{width:28px;height:26px;border:2px solid var(--yellow);display:flex;align-items:center;justify-content:center}
.copy{height:35px;background:var(--footer-bottom);text-align:center;font-size:13px;line-height:35px;color:#222}
</style>
</head>
<body>

<div class="topbar">
  <div class="wrap">
    <span><svg width="18" height="13" viewBox="0 0 18 13"><rect width="18" height="13" rx="1" fill="#f6c400"/><path d="M1 1l8 6 8-6" stroke="#0a9fe0" stroke-width="1.5" fill="none"/></svg>info@pinecrestlodgings.net</span>
    <span><svg width="15" height="15" viewBox="0 0 24 24"><path d="M6.6 10.8a15 15 0 006.6 6.6l2.2-2.2c.3-.3.7-.4 1-.2 1.1.4 2.3.6 3.6.6.6 0 1 .4 1 1V20c0 .6-.4 1-1 1C10.6 21 3 13.4 3 4c0-.6.4-1 1-1h3.5c.6 0 1 .4 1 1 0 1.3.2 2.5.6 3.6.1.3 0 .7-.2 1z" fill="#fff"/></svg>123-456-7890</span>
  </div>
</div>

<header class="header">
  <div class="wrap">
    <div class="brand">
      <div class="brand-name">PINECREST LODGINGS</div>
      <div class="brand-tag">COMPARE PRICES ON ACCOMMODATIONS IN BANFF</div>
    </div>
    <nav class="nav">
      <a class="active">HOME</a><a>BANFF HOTELS</a><a>BANFF RESORTS</a><a>LODGES</a><a>INNS &amp; MOTELS</a><a>CONTACT US</a>
    </nav>
  </div>
</header>

<section class="hero" role="img" aria-label="Photo of a canoe with paddlers on a turquoise mountain lake below forested peaks in Banff">
  <div class="hero-text">
    <h1>FIND THE BEST HOTEL DEALS ON PINECREST LODGINGS</h1>
    <p>Choose From Over 47 Hotels, Resorts And Inns In Banff</p>
  </div>
</section>

<section class="booking">
  <div class="wrap">
    <div class="booking-title">
      <svg width="42" height="42" viewBox="0 0 42 42"><circle cx="21" cy="21" r="18" fill="none" stroke="#f6c400" stroke-width="3"/><path d="M12 21l6 6 12-13" fill="none" stroke="#f6c400" stroke-width="3.5"/></svg>
      <div>CHECK<br>AVAILIBILITY</div>
    </div>
    <div class="field f-loc">Location<svg width="14" height="18" viewBox="0 0 14 18"><path d="M7 1a6 6 0 016 6c0 4-6 10-6 10S1 11 1 7a6 6 0 016-6z" fill="none" stroke="#888" stroke-width="1.5"/><circle cx="7" cy="7" r="2" fill="#888"/></svg></div>
    <div class="field f-date">Check In<svg width="16" height="16" viewBox="0 0 16 16"><rect x="1" y="2" width="14" height="13" fill="none" stroke="#888"/><path d="M1 6h14M4 9h2M8 9h2M11 9h2M4 12h2M8 12h2" stroke="#888"/></svg></div>
    <div class="field f-date">Check Out<svg width="16" height="16" viewBox="0 0 16 16"><rect x="1" y="2" width="14" height="13" fill="none" stroke="#888"/><path d="M1 6h14M4 9h2M8 9h2M11 9h2M4 12h2M8 12h2" stroke="#888"/></svg></div>
    <div class="field f-rooms">Rooms<svg width="12" height="8" viewBox="0 0 12 8"><path d="M1 1l5 5 5-5" fill="none" stroke="#666" stroke-width="1.5"/></svg></div>
    <div class="btn-check">CHECK AVAILIBILITY</div>
  </div>
</section>

<section class="welcome">
  <div class="wrap">
    <h2 class="sec-title">Welcome to <b>PINECREST LODGINGS</b></h2>
    <p class="welcome-text">Lorem ipsum dolor sit amet, consectetuer adipiscing elit, sed diam nonummy nibh eu mod tincidut ufgkdti laoreetna all dolore magna aliquam erat volutpat. Lorem ipsum dolor sit amet, consectetuer adipiscing elit, sed diam nonummy nibh euismod tincidut ufgkdti laoreetna all dolore magna aliquam erat volutpat. Ut wisi enim ad minim veniam, quis nostrud exe tationsequ ullamcor suscipitatci lobortis nisl ut aliquip ex ea commodo consequat. Duis autem vel eum iriure dolor inocc hendrerit in vulputat velitcaa all esse molestie consequat, vel illum dolore eu feugia. Lorem ipsum dolor sit amet, consectetuer adipiscing elit, sed diam nonummy nibh euismod tincidut ufgkdti laoreetna all dolore magna aliquam erat volutpat. Ut wisi enim ad minim veniam, quis nostrud exe tationsequ ullamcor.</p>
    <span class="btn btn-solid read-more">READ MORE</span>
    <aside class="weather">
      <div class="weather-top">
        <span class="city">VANCOUVER</span><span class="unit">°F °C</span>
        <svg style="position:absolute;top:50px;left:34px" width="62" height="62" viewBox="0 0 62 62"><circle cx="31" cy="31" r="13" fill="none" stroke="#fff" stroke-width="3"/><g stroke="#fff" stroke-width="3" stroke-linecap="round"><path d="M31 4v8M31 50v8M4 31h8M50 31h8M12 12l6 6M44 44l6 6M12 50l6-6M44 18l6-6"/></g></svg>
        <span class="temp">23°</span>
      </div>
      <div class="weather-days">
        <div class="day"><svg width="34" height="30" viewBox="0 0 34 30"><path d="M9 20a6 6 0 010-12 8 8 0 0115 2 5 5 0 010 10z" fill="none" stroke="#999" stroke-width="1.5"/><path d="M11 24l-2 4M17 24l-2 4M23 24l-2 4" stroke="#999" stroke-width="1.5"/></svg><br>MON</div>
        <div class="day"><svg width="34" height="30" viewBox="0 0 34 30"><path d="M9 22a6 6 0 010-12 8 8 0 0115 2 5 5 0 010 10z" fill="none" stroke="#999" stroke-width="1.5"/></svg><br>TUE</div>
        <div class="day"><svg width="34" height="30" viewBox="0 0 34 30"><circle cx="17" cy="15" r="6" fill="none" stroke="#999" stroke-width="1.5"/><g stroke="#999" stroke-width="1.5"><path d="M17 2v5M17 23v5M4 15h5M25 15h5M8 6l3 3M23 21l3 3M8 24l3-3M23 9l3-3"/></g></svg><br>WED</div>
      </div>
    </aside>
  </div>
</section>

<section class="featured">
  <div class="wrap">
    <h2 class="sec-title">FEATURED <b>HOTELS</b></h2>
    <div class="cards">
      <article class="card">
        <div class="card-img" role="img" aria-label="Photo of a snow-covered chalet resort with lit windows below mountains" style="background:linear-gradient(180deg,#c9d6e4,#8b6a52 70%,#eef2f5)"></div>
        <div class="card-head"><h3>Glacierview Springs Resort</h3><span class="price">$445 CAD</span></div>
        <div class="stars"><svg width="95" height="16" viewBox="0 0 95 16"><g fill="#f6b400"><path id="s" d="M8 0l2.4 5 5.4.6-4 3.7 1.1 5.4L8 12l-4.9 2.7 1.1-5.4-4-3.7L5.6 5z"/><use href="#s" x="19"/><use href="#s" x="38"/><use href="#s" x="57"/><use href="#s" x="76"/></g></svg></div>
        <p>Lorem ipsum dolor sit amet, consec lorem<b>2 Beds, 24 hr Room Service, many more...</b></p>
        <div class="card-actions"><span class="btn btn-line">VIEW DETAILS</span><span class="btn btn-solid">BOOK NOW</span></div>
      </article>
      <article class="card">
        <div class="card-img" role="img" aria-label="Photo of a timber resort building among pine trees at dusk" style="background:linear-gradient(180deg,#3d6fa8,#4d6a4a 55%,#6e5a45)">
          <svg class="badge" width="108" height="92" viewBox="0 0 108 92"><path d="M10 50L70 8l30 30-60 42z" fill="#f6c400"/><circle cx="82" cy="18" r="4" fill="#333"/><text x="52" y="52" transform="rotate(-35 52 52)" font-family="Oswald,Arial,sans-serif" font-size="20" fill="#1b7fcf" text-anchor="middle">41% OFF</text><text x="58" y="64" transform="rotate(-35 58 64)" font-family="Open Sans,Arial,sans-serif" font-size="9" fill="#222" text-anchor="middle">3 Nights/ 3 Days</text></svg>
        </div>
        <div class="card-head"><h3>Glacierview Springs Resort</h3><span class="price">$445 CAD</span></div>
        <div class="stars"><svg width="95" height="16" viewBox="0 0 95 16"><g fill="#f6b400"><use href="#s"/><use href="#s" x="19"/><use href="#s" x="38"/><use href="#s" x="57"/><use href="#s" x="76"/></g></svg></div>
        <p>Lorem ipsum dolor sit amet, consec lorem<b>2 Beds, 24 hr Room Service, many more...</b></p>
        <div class="card-actions"><span class="btn btn-line">VIEW DETAILS</span><span class="btn btn-solid">BOOK NOW</span></div>
      </article>
      <article class="card">
        <div class="card-img" role="img" aria-label="Photo of a large stone castle hotel in a snowy forest valley" style="background:linear-gradient(180deg,#9fb4c9,#7d8893 50%,#dfe5ea)"></div>
        <div class="card-head"><h3>Stonehaven Resort Hotel</h3><span class="price">$ 265 CAD</span></div>
        <div class="stars"><svg width="95" height="16" viewBox="0 0 95 16"><g fill="#f6b400"><use href="#s"/><use href="#s" x="19"/><use href="#s" x="38"/><use href="#s" x="57"/><use href="#s" x="76"/></g></svg></div>
        <p>Lorem ipsum dolor sit amet, consec lorem<b>2 Beds, 24 hr Room Service, many more...</b></p>
        <div class="card-actions"><span class="btn btn-line">VIEW DETAILS</span><span class="btn btn-solid">BOOK NOW</span></div>
      </article>
    </div>
    <div class="pager">
      <span><svg width="10" height="14" viewBox="0 0 10 14"><path d="M8 1L2 7l6 6" fill="none" stroke="#333" stroke-width="2"/></svg></span>
      <span><svg width="10" height="14" viewBox="0 0 10 14"><path d="M2 1l6 6-6 6" fill="none" stroke="#333" stroke-width="2"/></svg></span>
    </div>
  </div>
</section>

<section class="articles">
  <div class="wrap">
    <h2 class="sec-title">RECENT <b>ARTICLES</b></h2>
    <article class="lead">
      <div class="lead-img" role="img" aria-label="Photo of an ice sculpture on a frozen lake below snowy peaks" style="background:linear-gradient(180deg,#b9c6d3,#6f8597 45%,#d7e4ee)">
        <div class="date"><b>06</b><span>Jan</span></div>
      </div>
      <h3>ROMANTIC BANFF GETAWAY HOTELS</h3>
      <p>Banff consistently comes up when people talk about romantic locations in Canada. It's an idyllic village nestled in the Rocky Mountains about two hours drive from Calgary <span class="more">[...]</span></p>
    </article>
    <div class="list">
      <article class="item">
        <div class="item-img" role="img" aria-label="Photo of a couple relaxing in a pool" style="background:linear-gradient(180deg,#3b9ac8,#c99a7c)"><div class="date"><b>06</b><span>Jan</span></div></div>
        <div><h3>ROMANTIC BANFF GETAWAY HOTELS</h3><p>Banff consistently comes up when people talk about romantic locations in Canada. It's an idyllic village nestled in the Rocky Mountains about two hours drive from Calgary <span class="more">[...]</span></p></div>
      </article>
      <article class="item">
        <div class="item-img" role="img" aria-label="Photo of two dogs beside travel luggage" style="background:linear-gradient(180deg,#d9d4cc,#9a6a3e)"><div class="date"><b>06</b><span>Jan</span></div></div>
        <div><h3>BANFF PET FRIENDLY HOTELS</h3><p>Banff consistently comes up when people talk about romantic locations in Canada. It's an idyllic village nestled in the Rocky Mountains about two hours drive from Calgary<span class="more">[...]</span></p></div>
      </article>
      <article class="item">
        <div class="item-img" role="img" aria-label="Photo of a couple in a hot tub" style="background:linear-gradient(180deg,#e8e4dc,#c9a089)"><div class="date"><b>06</b><span>Jan</span></div></div>
        <div><h3>BANFF HOTELS WITH HOT-TUB</h3><p>Banff consistently comes up when people talk about romantic locations in Canada. It's an idyllic village nestled in the Rocky Mountains about two hours drive from Calgary <span class="more">[...]</span></p></div>
      </article>
    </div>
  </div>
</section>

<section class="why">
  <div class="wrap">
    <h2 class="sec-title">WHY BOOK WITH <b>PINECREST LODGINGS</b></h2>
    <div class="why-cols">
      <div class="why-col">
        <svg width="50" height="62" viewBox="0 0 50 62"><path d="M25 2a23 23 0 0123 23c0 16-23 35-23 35S2 41 2 25A23 23 0 0125 2z" fill="#f6c400"/><path d="M13 30h24M13 22v12M37 26v8M17 26h8v4" stroke="#0a9fe0" stroke-width="3" fill="none"/></svg>
        <h4>40,000+ Hotels In Canada</h4>
        <p>Lorem ipsum dolor sit amet, conctet, sed diam nibh eu mod volutpat nibh eu mod. <b>[...]</b></p>
      </div>
      <div class="why-col">
        <svg width="62" height="62" viewBox="0 0 62 62"><path d="M6 30L30 6h22v22L28 52z" fill="#f6c400"/><circle cx="43" cy="15" r="4" fill="#0a9fe0"/><text x="29" y="38" font-family="Oswald,Arial,sans-serif" font-size="18" fill="#0a9fe0" text-anchor="middle">$</text></svg>
        <h4>Best Price Guarantee</h4>
        <p>Lorem ipsum dolor sit amet, conctet, sed diam nibh eu mod volutpat nibh eu mod. <b>[...]</b></p>
      </div>
      <div class="why-col">
        <svg width="70" height="62" viewBox="0 0 70 62"><path d="M3 31C13 15 24 9 35 9s22 6 32 22C57 47 46 53 35 53S13 47 3 31z" fill="#f6c400"/><circle cx="35" cy="31" r="10" fill="#0a9fe0"/><path d="M12 55L58 7" stroke="#0a9fe0" stroke-width="5"/></svg>
        <h4>No Hidden Charges</h4>
        <p>Lorem ipsum dolor sit amet, conctet, sed diam nibh eu mod volutpat nibh eu mod. <b>[...]</b></p>
      </div>
      <div class="why-col">
        <svg width="62" height="62" viewBox="0 0 62 62"><rect x="10" y="14" width="40" height="26" rx="3" transform="rotate(-30 30 27)" fill="#f6c400"/><text x="30" y="33" transform="rotate(-30 30 27)" font-family="Oswald,Arial,sans-serif" font-size="16" fill="#0a9fe0" text-anchor="middle">$</text><path d="M10 56c8-6 16-10 28-8l12-4" stroke="#f6c400" stroke-width="5" fill="none"/></svg>
        <h4>Pay By Cash</h4>
        <p>Lorem ipsum dolor sit amet, conctet, sed diam nibh eu mod volutpat nibh eu mod. <b>[...]</b></p>
      </div>
    </div>
  </div>
</section>

<section class="news">
  <div class="wrap">
    <h2>SUBSCRIBE TO OUR NEWSLETTER</h2>
    <div class="news-form"><span>Enter Your Email</span><i><svg width="20" height="18" viewBox="0 0 20 18"><path d="M1 8L19 1l-4 16-5-6z" fill="#fff"/></svg></i></div>
    <div class="follow">
      <span class="label">Follow US:</span>
      <span class="social"><i></i>Chatterly</span>
      <span class="social"><i></i>Circlia</span>
      <span class="social"><i></i>Quibbit</span>
    </div>
  </div>
</section>

<footer class="footer" role="img" aria-label="Footer background photo of a pine forest by a river">
  <div class="wrap">
    <div class="f-cols">
      <div class="f-col f-explore">
        <h5>Explore <b>Banff</b></h5>
        <ul><li>Things to do in Banff</li><li>Banff Festivals</li><li>Experience Summit Skyride</li><li>Heli Sightseeing in Banff</li><li>Hiking in Banff</li><li>Camping &amp; Campgrounds</li><li>Hotels near Alpine Hot Pools</li><li>Nearby Cities</li></ul>
      </div>
      <div class="f-col f-quick">
        <h5>Quick <b>Links</b></h5>
        <ul><li>Home</li><li>Banff Hotels</li><li>Banff Resorts</li><li>Lodges</li><li>Inn &amp; Motels</li><li>Contact Us</li></ul>
      </div>
      <div class="f-col f-contact">
        <h5>Contact <b>Details</b></h5>
        <div class="c-row"><i><svg width="10" height="13" viewBox="0 0 10 13"><path d="M5 0a5 5 0 015 5c0 3-5 8-5 8S0 8 0 5a5 5 0 015-5z" fill="#1f7ea4"/></svg></i><span>Lorem ipsum, Dollar smit,<br>City Code - 12345</span></div>
        <div class="c-row"><i><svg width="12" height="12" viewBox="0 0 24 24"><path d="M6.6 10.8a15 15 0 006.6 6.6l2.2-2.2c.3-.3.7-.4 1-.2 1.1.4 2.3.6 3.6.6.6 0 1 .4 1 1V20c0 .6-.4 1-1 1C10.6 21 3 13.4 3 4c0-.6.4-1 1-1h3.5c.6 0 1 .4 1 1 0 1.3.2 2.5.6 3.6.1.3 0 .7-.2 1z" fill="#1f7ea4"/></svg></i><span>123-456-7890</span></div>
        <div class="c-row"><i><svg width="12" height="9" viewBox="0 0 12 9"><rect width="12" height="9" fill="#1f7ea4"/><path d="M0 0l6 5 6-5" stroke="#fff" fill="none"/></svg></i><span>info@companyname.com</span></div>
      </div>
      <div class="f-col f-gallery">
        <h5>Our <b>Gallery</b></h5>
        <div class="gallery">
          <div role="img" aria-label="Gallery photo of a castle hotel" style="background:linear-gradient(#8fa3b8,#6b5a4a)"></div>
          <div role="img" aria-label="Gallery photo of a hotel bedroom" style="background:linear-gradient(#d8cdbb,#8a6e55)"></div>
          <div role="img" aria-label="Gallery photo of a lobby at night" style="background:linear-gradient(#5a3e2b,#c48a4a)"></div>
          <div role="img" aria-label="Gallery photo of a mountain town" style="background:linear-gradient(#3d6fb0,#c9d4de)"></div>
        </div>
        <div class="g-arrows">
          <span><svg width="8" height="12" viewBox="0 0 8 12"><path d="M7 1L2 6l5 5" fill="none" stroke="#f6c400" stroke-width="2"/></svg></span>
          <span><svg width="8" height="12" viewBox="0 0 8 12"><path d="M1 1l5 5-5 5" fill="none" stroke="#f6c400" stroke-width="2"/></svg></span>
        </div>
      </div>
    </div>
  </div>
</footer>
<div class="copy">Copyright 2015 Pinecrest Lodgings. All Rights Reserved.</div>

</body>
</html>
```